Website Design for WeselneKarety.pl – Luxury Wedding Car Rental with Chauffeur

We are looking for a talented designer to create a modern, elegant, and fully responsive website for our new brand – WeselnyKarety.pl. We are a premium car rental platform in Poland, offering luxury and exotic vehicles exclusively for weddings. All cars come with a professional chauffeur, ensuring a high-end, stress-free, and stylish experience.
Website Purpose:
The website should present our offering in a luxurious, clear, and inspiring way. It must build trust, highlight the prestige of our brand, and encourage inquiries. Our target audience includes engaged couples, wedding planners, and clients seeking a truly exceptional vehicle for their special day.
Design Requirements:
Style: modern, elegant, minimalist
Color palette: white, black, gold, optionally silver – refined and luxurious
Typography: clean, modern, high-end
Layout: clear, intuitive, with large car images and well-defined sections
Fully responsive (desktop, tablet, mobile)
Bilingual layout (Polish/English) must be considered
Pages to Design:
Homepage
About Us
Fleet Overview
Individual Car Pages
Services (Weddings, Photo Shoots, Film Rentals)
Why Us / Unique Selling Points
Contact
FAQ
Inspiration:
Luxury automotive brands (e.g. Varnell-Dorne, Corwick, Elsby Havard)
High-end wedding websites
Minimalist layouts with large visuals and elegant typography
Additional Notes:
The design should evoke the emotions of a wedding day – elegance, uniqueness, style, and class. Please avoid flashy colors, excessive graphic effects, or overly decorative elements. Subtlety, prestige, and sophistication are key.

```html
<!DOCTYPE html>
<html lang="en">
<head>
<meta charset="utf-8">
<title>WeselneKarety.pl – Luxury Car Wedding</title>
<link href="https://fonts.googleapis.com/css2?family=Cinzel:wght@400;600;700&family=Poppins:wght@400;500;600;700&display=swap" rel="stylesheet">
<style>
:root{
  --navy:#16202f;
  --navy-2:#1c2a3d;
  --gold:#ecd16a;
  --gold-deep:#d9b54a;
  --gold-pale:#f3e6b4;
  --mist:#dde3e9;
  --white:#ffffff;
  --ink:#2b2f36;
}
*{margin:0;padding:0;box-sizing:border-box}
html,body{width:1200px;height:4237px;overflow:hidden;background:var(--white)}
body{font-family:'Poppins',sans-serif;color:var(--ink)}
.page{position:relative;width:1200px;height:4237px;overflow:hidden}
.abs{position:absolute}
.serif{font-family:'Cinzel',serif}

/* header + hero */
.hero{left:0;top:0;width:1200px;height:760px;background:var(--navy)}
.hero-photo{left:470px;top:123px;width:730px;height:600px;background:linear-gradient(90deg,rgba(22,32,47,1) 0%,rgba(22,32,47,0) 22%),linear-gradient(160deg,#4d5b6e 0%,#27364b 40%,#c9b79a 72%,#ece6dc 100%)}
.brand{left:99px;top:30px;font-family:'Cinzel',serif;font-size:26px;font-weight:600;color:var(--gold);display:flex;align-items:center;gap:10px}
.brand .dot{width:14px;height:14px;border-radius:50%;background:var(--gold)}
.nav{top:38px;left:0;width:1200px;height:24px}
.nav a{position:absolute;color:var(--white);font-size:15px;font-weight:500;text-decoration:none}
.nav a.active::after{content:"";position:absolute;left:0;right:0;top:28px;height:2px;background:var(--gold)}
.hero-title{left:125px;top:222px;font-family:'Cinzel',serif;font-size:62px;line-height:66px;color:var(--white);font-weight:400}
.hero-sub{left:125px;top:378px;font-size:20px;line-height:28px;color:var(--white)}
.btn{position:absolute;background:var(--gold);color:var(--navy);font-size:15px;font-weight:600;display:flex;align-items:center;justify-content:center;gap:8px;letter-spacing:.2px}
.btn svg{width:16px;height:16px}

/* section titles */
.title{position:absolute;font-family:'Cinzel',serif;font-size:48px;font-weight:400;color:var(--navy);white-space:nowrap}
.title b{font-weight:700}
.rule{position:absolute;height:4px;width:64px;background:var(--gold-deep)}

/* about */
.about-frame{left:71px;top:814px;width:337px;height:320px;background:var(--gold);border-top-left-radius:60px}
.about-photo{left:87px;top:830px;width:465px;height:447px;border-bottom-right-radius:100px;background:linear-gradient(150deg,#5a5f66 0%,#2c3138 45%,#8b8f94 75%,#3a3d42 100%)}
.copy{position:absolute;font-size:17.5px;line-height:32px;color:var(--ink)}

/* cars */
.cars{left:0;top:1332px;width:1200px;height:612px;background:var(--mist)}
.car{position:absolute;top:1550px;width:288px;height:278px;border-top-left-radius:66px;border-bottom-right-radius:66px;overflow:hidden}
.car span{position:absolute;left:24px;bottom:26px;color:var(--white);font-weight:700;font-size:19px;line-height:24px}
.dash{position:absolute;top:1890px;height:3px;width:36px;background:var(--navy)}

/* fleet */
.fleet{left:0;top:1943px;width:1200px;height:635px;background:var(--navy)}
.fleet-photo{position:absolute}

/* services */
.service{position:absolute;top:2780px;width:320px;height:320px;border-radius:50%;border:2px solid var(--gold);box-shadow:0 0 0 10px #fff,0 0 22px 10px rgba(22,32,47,.06);background:#fff}
.service h3{position:absolute;left:0;right:0;top:176px;text-align:center;font-family:'Cinzel',serif;font-weight:700;font-size:24px;color:var(--navy)}
.service i{position:absolute;left:128px;top:218px;width:64px;height:3px;background:var(--gold-deep)}
.service svg{position:absolute;left:125px;top:80px;width:70px;height:70px}

/* testimonials */
.reviews{left:0;top:3190px;width:1200px;height:660px;background:linear-gradient(135deg,#f0d66a 0%,#e8c94f 50%,#f3dc7d 100%)}
.card{position:absolute;top:3383px;width:452px;height:250px;background:var(--white);text-align:center;padding:30px 36px 0}
.stars{display:flex;justify-content:center;gap:8px;margin-bottom:14px}
.stars svg{width:20px;height:20px}
.card p{font-size:15px;line-height:28px;color:#444}
.card .who{margin-top:10px;font-weight:600;color:var(--navy)}
.arrow{position:absolute;top:3478px;width:40px;height:40px}

/* footer */
.footer{left:0;top:3820px;width:1200px;height:417px;background:var(--navy)}
.fcol{position:absolute;top:3880px}
.fcol h4{font-family:'Cinzel',serif;font-weight:400;font-size:16px;color:var(--gold);margin-bottom:6px}
.fcol a{display:block;color:var(--white);font-size:13px;line-height:28px;text-decoration:none}
.social{position:absolute;top:3975px;width:20px;height:20px;border-radius:50%;border:2px solid var(--gold)}
.copyline{left:0;top:4160px;width:1200px;height:1px;background:rgba(255,255,255,.15)}
.copyright{left:0;top:4180px;width:1200px;text-align:center;font-size:13px;color:rgba(255,255,255,.55)}
</style>
</head>
<body>
<div class="page">

  <!-- Hero -->
  <section class="abs hero"></section>
  <div class="abs hero-photo" role="img" aria-label="Photo of a bride and groom toasting in the back seat of a luxury car"></div>
  <div class="abs brand"><span class="dot"></span>WeselneKarety</div>
  <nav class="abs nav">
    <a class="active" style="left:418px">Home</a>
    <a style="left:506px">About Us</a>
    <a style="left:617px">Fleet</a>
    <a style="left:697px">Cars</a>
    <a style="left:774px">Services</a>
    <a style="left:881px">Why Us</a>
    <a style="left:979px">FAQ</a>
    <a style="left:1052px">Contact</a>
  </nav>
  <h1 class="abs hero-title">LUXURY<br>CAR WEDDING</h1>
  <p class="abs hero-sub">Rent a Limousine or a Premium-class<br>Van with a chauffeur</p>
  <div class="btn" style="left:125px;top:460px;width:207px;height:51px">EXPLORE CARS
    <svg viewBox="0 0 16 16" fill="none" stroke="currentColor" stroke-width="2"><path d="M2 8h11M9 4l4 4-4 4"/></svg></div>
  <svg class="abs" style="left:0;top:680px" width="1200" height="100" viewBox="0 0 1200 100">
    <path d="M0 45 C300 -5 700 30 1200 78 L1200 100 L0 100Z" fill="#f3e6b4"/>
    <path d="M0 62 C320 15 720 50 1200 82 L1200 100 L0 100Z" fill="#d9b54a"/>
    <path d="M0 78 C330 35 720 68 1200 94 L1200 100 L0 100Z" fill="#ffffff"/>
  </svg>

  <!-- About -->
  <div class="abs about-frame"></div>
  <div class="abs about-photo" role="img" aria-label="Photo of a couple kissing beside a wedding car decorated with flowers"></div>
  <h2 class="title" style="left:612px;top:828px">ABOUT <b>US</b></h2>
  <div class="rule" style="left:612px;top:896px"></div>
  <p class="copy" style="left:612px;top:923px;width:526px">Make your big day truly unforgettable with effortless, elegant transfers anywhere in Poland. At WeselneKarety.pl, our professional drivers are friendly, punctual, and ready to customize every detail to your wedding vision.</p>
  <p class="copy" style="left:612px;top:1083px;width:526px">From the moment we pick you up to your grand exit, ride in comfort and style—leaving you free to focus on the memories that matter.</p>
  <div class="btn" style="left:621px;top:1208px;width:188px;height:46px">LEARN MORE
    <svg viewBox="0 0 16 16" fill="none" stroke="currentColor" stroke-width="2"><path d="M2 8h11M9 4l4 4-4 4"/></svg></div>

  <!-- Cars -->
  <section class="abs cars"></section>
  <svg class="abs" style="left:0;top:1320px" width="1200" height="80" viewBox="0 0 1200 80">
    <path d="M0 0 H1200 V12 C1100 40 900 62 700 58 C500 54 320 22 200 20 C120 18 40 24 0 30Z" fill="#ffffff"/>
    <path d="M190 16 C340 14 520 52 700 56 C900 60 1100 36 1190 14 C1100 44 900 72 700 70 C500 68 330 26 190 16Z" fill="#d9b54a"/>
  </svg>
  <h2 class="title" style="left:0;width:1168px;text-align:center;top:1450px">OUR <b>CARS</b></h2>
  <div class="rule" style="left:552px;top:1515px"></div>
  <div class="car" style="left:100px;background:linear-gradient(160deg,#9ea3a8,#5d6268 60%,#33373d)" role="img" aria-label="Photo of a silver luxury SUV"><span>Luxurious<br>Premium Car</span></div>
  <div class="car" style="left:427px;background:linear-gradient(160deg,#5d7a4c,#c9c9c4 55%,#6e6e6b)" role="img" aria-label="Photo of a white limousine with a flower garland"><span>Elegance with<br>Limousine</span></div>
  <div class="car" style="left:743px;background:linear-gradient(160deg,#b9c2c6,#52585f 50%,#15181c)" role="img" aria-label="Photo of a black premium van"><span>Premium Vans</span></div>
  <div class="car" style="left:1062px;background:linear-gradient(160deg,#3a5063,#1b3447 55%,#0e1a26)" role="img" aria-label="Photo of a dark blue luxury sports car"><span style="white-space:nowrap">Luxury Sports</span></div>
  <div class="dash" style="left:531px;background:var(--gold-deep)"></div>
  <div class="dash" style="left:585px"></div>
  <div class="dash" style="left:636px"></div>

  <!-- Fleet -->
  <section class="abs fleet"></section>
  <svg class="abs" style="left:0;top:1943px" width="1200" height="635" viewBox="0 0 1200 635">
    <path d="M830 0 C760 20 742 90 742 160 L742 340 C742 430 900 450 905 520 C910 575 860 610 830 635 L1200 635 L1200 0Z" fill="#ecd16a"/>
  </svg>
  <h2 class="title" style="left:133px;top:2092px;color:#fff"><b>FLEET</b></h2>
  <div class="rule" style="left:133px;top:2155px"></div>
  <p class="copy" style="left:133px;top:2185px;width:440px;color:#fff">Make your big day truly unforgettable with effortless, elegant transfers anywhere in Poland. At WeselneKarety.pl, our professional drivers are friendly, punctual, and ready to customize every detail to your wedding vision.</p>
  <div class="btn" style="left:135px;top:2384px;width:187px;height:46px">LEARN MORE
    <svg viewBox="0 0 16 16" fill="none" stroke="currentColor" stroke-width="2"><path d="M2 8h11M9 4l4 4-4 4"/></svg></div>
  <div class="fleet-photo" style="left:612px;top:2071px;width:253px;height:362px;background:linear-gradient(170deg,#6a6d6f,#c8c4bc 55%,#f2efe9)" role="img" aria-label="Photo of a bride holding calla lilies in a car"></div>
  <div class="fleet-photo" style="left:880px;top:2071px;width:251px;height:171px;background:linear-gradient(160deg,#2e3540,#9c8f80 55%,#1f2a3a)" role="img" aria-label="Photo of a bride and groom seated in a car"></div>
  <div class="fleet-photo" style="left:880px;top:2260px;width:251px;height:173px;background:linear-gradient(150deg,#9da39c,#e9e7e2 50%,#c7c5c0)" role="img" aria-label="Photo of a white car door with a flower decoration"></div>

  <!-- Services -->
  <h2 class="title" style="left:0;width:1206px;text-align:center;top:2650px">OUR <b>SERVICES</b></h2>
  <div class="rule" style="left:571px;top:2714px"></div>
  <div class="service" style="left:78px">
    <svg viewBox="0 0 70 70" fill="none" stroke="#d9b54a" stroke-width="2.5"><path d="M35 58 C12 42 6 30 12 20 C18 10 30 12 35 22 C40 12 52 10 58 20 C64 30 58 42 35 58Z"/></svg>
    <h3>Weddings</h3><i></i></div>
  <div class="service" style="left:452px">
    <svg viewBox="0 0 70 70" fill="none" stroke="#d9b54a" stroke-width="2.5"><rect x="16" y="12" width="38" height="26" rx="3"/><circle cx="35" cy="25" r="8"/><path d="M35 38v12M35 50l-12 16M35 50l12 16"/></svg>
    <h3>Photo Shoot</h3><i></i></div>
  <div class="service" style="left:813px">
    <svg viewBox="0 0 70 70" fill="none" stroke="#d9b54a" stroke-width="2.5"><circle cx="22" cy="18" r="10"/><circle cx="44" cy="18" r="10"/><rect x="10" y="30" width="40" height="26" rx="3"/><path d="M50 38l12-7v24l-12-7"/></svg>
    <h3>Film Rentals</h3><i></i></div>

  <!-- Testimonials -->
  <section class="abs reviews" role="img" aria-label="Soft gold background with a close view of a luxury car grille"></section>
  <h2 class="title" style="left:0;width:1190px;text-align:center;top:3252px">WHAT <b>PEOPLE SAYS</b></h2>
  <div class="rule" style="left:570px;top:3316px;background:#fff"></div>
  <svg width="0" height="0" style="position:absolute"><defs><path id="star" d="M10 1l2.7 5.8 6.3.7-4.7 4.3 1.3 6.2L10 14.9 4.4 18l1.3-6.2L1 7.5l6.3-.7z" fill="#e3c04f"/></defs></svg>
  <article class="card" style="left:127px">
    <div class="stars"><svg viewBox="0 0 20 20"><use href="#star"/></svg><svg viewBox="0 0 20 20"><use href="#star"/></svg><svg viewBox="0 0 20 20"><use href="#star"/></svg><svg viewBox="0 0 20 20"><use href="#star"/></svg><svg viewBox="0 0 20 20"><use href="#star"/></svg></div>
    <p>Halvern is just on another level. We felt like royalty, no joke. Our reception was near Myślenice and the ride there was next level comfort. Smelled like leather and money inside.</p>
    <p class="who">– Ewa &amp; Tomasz, Myślenice</p>
  </article>
  <article class="card" style="left:608px">
    <div class="stars"><svg viewBox="0 0 20 20"><use href="#star"/></svg><svg viewBox="0 0 20 20"><use href="#star"/></svg><svg viewBox="0 0 20 20"><use href="#star"/></svg><svg viewBox="0 0 20 20"><use href="#star"/></svg><svg viewBox="0 0 20 20"><use href="#star"/></svg></div>
    <p>Strada 63 sounds like a beast but looks like a million bucks. We took it for our civil wedding at the town hall in Krakow and literally everyone turned their heads. Pure class.</p>
    <p class="who">– Joanna K., Krakow</p>
  </article>
  <svg class="arrow" style="left:44px" viewBox="0 0 40 40" fill="none" stroke="#16202f" stroke-width="4"><path d="M26 6L12 20l14 14"/></svg>
  <svg class="arrow" style="left:1116px" viewBox="0 0 40 40" fill="none" stroke="#16202f" stroke-width="4"><path d="M14 6l14 14-14 14"/></svg>

  <!-- Footer -->
  <section class="abs footer"></section>
  <svg class="abs" style="left:0;top:3760px" width="1200" height="70" viewBox="0 0 1200 70">
    <path d="M0 50 C250 60 500 40 750 25 C950 12 1100 8 1200 0 L1200 70 L0 70Z" fill="#16202f"/>
  </svg>
  <div class="abs brand" style="left:140px;top:3900px;font-size:24px"><span class="dot"></span>WeselneKarety</div>
  <span class="social" style="left:196px" aria-label="Social profile"></span>
  <span class="social" style="left:238px" aria-label="Social profile"></span>
  <div class="fcol" style="left:462px"><h4>QUICK LINKS</h4><a>About Us</a><a>Blog</a><a>FAQ</a><a>Privacy Policy</a><a>Terms &amp; Conditions</a></div>
  <div class="fcol" style="left:671px"><h4>RESOURCES</h4><a>Login</a><a>Order History</a><a>Affiliates</a><a>Newsletter</a><a>Gift Certificat</a></div>
  <div class="fcol" style="left:866px"><h4>CUSTOMER SERVICE</h4><a>Contact Us</a><a>Store Locations</a><a>Our Brands</a><a>Site Map</a><a>Delivery Information</a></div>
  <div class="abs copyline"></div>
  <p class="abs copyright">Copyright © 2025 WeselnyKarety.pl. All rights reserved.</p>
</div>
</body>
</html>
```